Build a Web page - Dovin Pratchell Homes, LLC - a custom home builder

We are a custom home builder in Wisconsin. Need a basic web page with a home page, About Us, Contact info, Gallery, and Testimonials page. Gallery will probably have sub-pages and each will have about ten pictures or less. I already own the domain and have web hosting through Wix, I just need the site built. Once the page is built I should be able to do the upkeep on it myself. If I need to add pictures or whatever.
Updates

Project Deadline Extended
Reason: I am still looking through designs and will select soon - thank you!

Target Market(s)

Gen X and Millennials who are looking to build a home. Custom built homes - not generic spec homes.

Industry/Entity Type

Home Builder

Number of Pages Required

5+ page

Font styles to use
Sans Serif

Colors
ffffff
ec1f27
000000
9d9d9d

Requirements
Must have
• I have no idea if I want coded or in coded. I'm not sure of the difference and why I would want one over the other.
Nice to have
• We like the following colors - red, black, gray, white.
Should not have
• not a big fan of clip art like hammers, tape measures, etc. Must look professional.

```html
<!DOCTYPE html>
<html lang="en">
<head>
<meta charset="utf-8">
<title>Dovin Pratchell Homes, LLC</title>
<link href="https://fonts.googleapis.com/css2?family=Raleway:wght@300;400;600;700&family=Open+Sans:wght@400;600&family=Montserrat:wght@400;500&display=swap" rel="stylesheet">
<style>
:root{
  --red:#8e0f15;
  --red-bright:#c1272d;
  --ink:#333333;
  --muted:#6f6f6f;
  --grey:#9d9d9d;
  --band:#efefef;
  --footer:#231f20;
  --white:#ffffff;
}
*{margin:0;padding:0;box-sizing:border-box}
html,body{width:1200px;height:3255px;overflow:hidden;background:var(--white)}
body{position:relative;font-family:"Open Sans",sans-serif;color:var(--ink)}
.abs{position:absolute}

/* hero */
.hero-photo{left:0;top:0;width:1200px;height:700px;
  background:linear-gradient(180deg,#8a7260 0%,#b79f86 30%,#a3473f 55%,#c9b8a6 75%,#ffffff 100%);
  clip-path:polygon(0 0,1200px 0,1200px 585px,1059px 603px,831px 677px,608px 571px,380px 690px,152px 586px,0 560px)}
.hero-fade{left:0;top:480px;width:1200px;height:260px;background:linear-gradient(180deg,rgba(255,255,255,0) 0%,rgba(255,255,255,.85) 60%,#fff 100%)}
.hero-line{left:0;top:0}

/* header */
.site-header{left:87px;top:30px;width:1028px;height:109px;background:var(--white);box-shadow:0 1px 4px rgba(0,0,0,.12)}
.brand{left:10px;top:8px;width:100px;height:92px;border:3px solid #8c8c8c;display:flex;flex-direction:column;align-items:center;justify-content:center;gap:4px}
.brand-square{width:14px;height:14px;background:var(--red-bright)}
.brand-name{font-family:"Raleway",sans-serif;font-weight:600;font-size:11px;line-height:1.15;color:#555;text-align:center;text-transform:uppercase}
.contact-strip{left:486px;top:24px;font-size:13px;color:#444;display:flex;align-items:center;gap:8px}
.contact-strip strong{color:var(--red-bright);font-weight:600}
.social{left:866px;top:20px;display:flex;gap:5px}
.social span{width:22px;height:22px;border:1.5px solid #666;border-radius:50%}
.main-nav{left:419px;top:70px;display:flex;gap:42px;font-family:"Montserrat",sans-serif;font-size:12px;letter-spacing:1.5px;color:#666}
.main-nav .current{color:var(--red-bright)}

/* about */
.about-rule{left:203px;top:680px;width:2px;height:710px;background:var(--red)}
.about-tab{left:180px;width:52px;background:var(--red);display:flex;align-items:center;justify-content:center}
.about-tab.top{top:760px;height:66px;clip-path:polygon(0 0,100% 0,100% 100%,50% 88%,0 100%);}
.about-tab.bottom{top:1198px;height:116px;clip-path:polygon(0 0,100% 0,100% 72%,50% 100%,0 72%)}
.about-photo{left:108px;top:829px;width:285px;height:367px;background:linear-gradient(160deg,#d7dde3 0%,#b8c2cc 45%,#b43a34 75%,#8c2a26 100%)}
.about-title{left:477px;top:748px;font-family:"Raleway",sans-serif;font-weight:300;font-size:66px;color:var(--red);letter-spacing:1px}
.about-text{left:477px;top:840px;width:592px;font-size:13.5px;line-height:22px;color:#555;text-align:justify}
.about-text p+p{margin-top:22px}
.btn-details{left:477px;top:1074px;width:209px;height:52px;background:#8a8a8a;color:#f2f2f2;font-family:"Raleway",sans-serif;font-size:18px;display:flex;align-items:center;justify-content:center}

/* projects band */
.projects-band{left:0;top:1389px;width:1200px;height:211px;background:var(--band);text-align:center}
.projects-kicker{position:absolute;left:0;right:0;top:60px;font-family:"Raleway",sans-serif;font-size:34px;color:#444}
.projects-title{position:absolute;left:0;right:0;top:112px;font-family:"Raleway",sans-serif;font-weight:700;font-size:38px;color:var(--red)}

/* gallery */
.gallery{left:0;top:1600px;width:1200px;height:538px;display:grid;grid-template-columns:repeat(4,300px);grid-template-rows:repeat(2,269px)}
.gallery-item{border:1px solid #fff;position:relative}
.g1{background:linear-gradient(180deg,#cfd6dc 0%,#cdb89d 50%,#6f8a3a 100%)}
.g2{background:linear-gradient(160deg,#d8c7a8 0%,#8c3a30 60%,#b7a58c 100%)}
.g3{background:linear-gradient(180deg,#c39a83,#a36f5c)}
.g4{background:linear-gradient(160deg,#e7dccb 0%,#6b3f23 55%,#3a2a22 100%)}
.g5{background:linear-gradient(180deg,#d6d2a5 0%,#e8e4dc 50%,#b08a5c 100%)}
.g6{background:linear-gradient(180deg,#cfc4b4 0%,#9a5a2a 50%,#6a3a1c 100%)}
.g7{background:linear-gradient(180deg,#cdc3b2 0%,#2a2624 40%,#a0704a 100%)}
.g8{background:linear-gradient(160deg,#b38d61 0%,#6e4428 50%,#2a3f40 100%)}
.gallery-overlay{position:absolute;inset:8px;background:rgba(160,20,28,.78);display:flex;align-items:center;justify-content:center;gap:12px}
.gallery-overlay span{width:40px;height:40px;border:1.5px solid #fff;display:flex;align-items:center;justify-content:center}

/* testimonials */
.testimonials-title{left:0;width:1200px;top:2240px;text-align:center;font-family:"Raleway",sans-serif;font-weight:600;font-size:36px;color:#333}
.quote{width:430px;padding:28px 56px 0 60px;color:#fff;font-family:"Raleway",sans-serif;font-size:14.5px;line-height:26px}
.quote.red{left:176px;top:2352px;height:137px;background:var(--red-bright)}
.quote.grey{left:584px;top:2378px;height:135px;background:#9a9a9a}
.quote-tail{position:absolute;bottom:-22px;width:0;height:0;border-top:22px solid;border-left:24px solid transparent}
.quote.red .quote-tail{left:290px;border-top-color:var(--red-bright)}
.quote.grey .quote-tail{left:290px;border-top-color:#9a9a9a}
.author{display:flex;align-items:center;gap:12px}
.avatar{width:40px;height:40px;border-radius:50%;background:linear-gradient(160deg,#c7b4a6,#5a4a44)}
.author-name{font-family:"Raleway",sans-serif;font-weight:600;font-size:15px;color:#333}
.author-role{font-size:11.5px;color:#999;margin-top:4px}
.slider-arrow{width:42px;height:42px;border:1.5px solid #ddd;border-radius:50%;display:flex;align-items:center;justify-content:center}

/* footer */
.site-footer{left:0;top:2726px;width:1200px;height:529px;background:var(--footer)}
.footer-map{left:620px;top:2910px;width:480px;height:280px;background:radial-gradient(ellipse at center,rgba(255,255,255,.09) 0%,rgba(255,255,255,0) 70%)}
.footer-brand{left:560px;top:2769px;width:106px;height:96px;border:3px solid #8c8c8c;display:flex;flex-direction:column;align-items:center;justify-content:center;gap:4px}
.footer-brand .brand-name{color:#bdbdbd}
.footer-rule{left:191px;top:2893px;width:851px;height:1px;background:#444}
.field{left:193px;width:365px;background:#f2f2f2;font-size:11px;color:#777;padding:8px 10px}
.f-name{top:2938px;height:37px}
.f-email{top:2990px;height:37px}
.f-message{top:3040px;height:91px}
.btn-send{left:193px;top:3149px;width:365px;height:37px;background:var(--red-bright);color:#fff;font-family:"Montserrat",sans-serif;font-weight:500;font-size:12px;letter-spacing:1px;display:flex;align-items:center;justify-content:center}
.contact-title{left:634px;top:2932px;font-family:"Raleway",sans-serif;font-weight:600;font-size:27px;color:#fff;letter-spacing:1px}
.contact-line{left:634px;display:flex;align-items:flex-start;gap:14px;color:#e6e6e6;font-size:16px}
.contact-line svg{flex:none;margin-top:2px}
.c-phone{top:2993px}
.c-mail{top:3035px}
.c-addr{top:3075px;font-size:12.5px;line-height:17px;text-transform:uppercase}
.copyright{left:640px;top:3166px;font-size:14px;color:#e6e6e6}
</style>
</head>
<body>

<div class="abs hero-photo" role="img" aria-label="Photo of a furnished master bedroom with a red patterned bedspread"></div>
<div class="abs hero-fade"></div>
<svg class="abs hero-line" width="1200" height="720" viewBox="0 0 1200 720">
  <polyline points="0,560 152,586 380,690 608,571 831,677 1059,603 1200,585" fill="none" stroke="#9a9a9a" stroke-width="2"/>
  <g fill="#fff" stroke="#8a8a8a" stroke-width="2">
    <circle cx="152" cy="586" r="6"/><circle cx="380" cy="690" r="6"/><circle cx="608" cy="571" r="6"/><circle cx="831" cy="677" r="6"/><circle cx="1059" cy="603" r="6"/>
  </g>
</svg>

<header class="abs site-header">
  <div class="abs brand"><span class="brand-square"></span><span class="brand-name">Dovin<br>Pratchell<br>Homes</span></div>
  <div class="abs contact-strip">
    <svg width="18" height="18" viewBox="0 0 24 24"><path d="M6.6 10.8a15 15 0 0 0 6.6 6.6l2.2-2.2c.3-.3.7-.4 1-.2 1.1.4 2.3.6 3.6.6.6 0 1 .4 1 1V20c0 .6-.4 1-1 1A17 17 0 0 1 3 4c0-.6.4-1 1-1h3.5c.6 0 1 .4 1 1 0 1.3.2 2.5.6 3.6.1.3 0 .7-.2 1z" fill="#222"/></svg>
    <strong>Any Questions</strong><span>Call us now on 1300 482 716</span>
  </div>
  <div class="abs social"><span></span><span></span><span></span><span></span><span></span></div>
  <nav class="abs main-nav"><span class="current">HOME</span><span>ABOUT US</span><span>CONTACT US</span><span>GALLERY</span><span>TESTIMONIALS</span></nav>
</header>

<section>
  <div class="abs about-rule"></div>
  <div class="abs about-tab top"><svg width="16" height="10" viewBox="0 0 16 10"><polyline points="2,2 8,8 14,2" fill="none" stroke="#fff" stroke-width="2"/></svg></div>
  <div class="abs about-photo" role="img" aria-label="Portrait of the home builder in a plaid shirt"></div>
  <div class="abs about-tab bottom"><svg width="16" height="10" viewBox="0 0 16 10" style="margin-top:34px"><polyline points="2,2 8,8 14,2" fill="none" stroke="#fff" stroke-width="2"/></svg></div>
  <h1 class="abs about-title">About Us</h1>
  <div class="abs about-text">
    <p>Lorem Ipsum is simply dummy text of the printing and typesetting industry. Lorem Ipsum has been the industry's standard dummy text ever since the 1500s, when an unknown printer took a galley of type and scrambled it to make a type specimen book. It has survived not only five centuries, but also the leap into electronic typesetting, remaining essentially unchanged.</p>
    <p>It was popularised in the 1960s with the release of Letraset sheets containing Lorem Ipsum passages, and more recently with desktop publishing software like Aldus PageMaker including versions of Lorem Ipsum.</p>
  </div>
  <div class="abs btn-details">Learn Details</div>
</section>

<section class="abs projects-band">
  <p class="projects-kicker">Successfully Delivering Projects</p>
  <h2 class="projects-title">Buy or Build a High Performance Home</h2>
</section>

<section class="abs gallery">
  <div class="gallery-item g1" role="img" aria-label="Photo of a home exterior with a patio and lawn"></div>
  <div class="gallery-item g2" role="img" aria-label="Photo of a living room with a fireplace"></div>
  <div class="gallery-item g3" role="img" aria-label="Photo of a house exterior">
    <div class="gallery-overlay">
      <span><svg width="16" height="16" viewBox="0 0 16 16"><circle cx="7" cy="7" r="4.5" fill="none" stroke="#fff" stroke-width="2"/><line x1="10.5" y1="10.5" x2="14" y2="14" stroke="#fff" stroke-width="2"/></svg></span>
      <span><svg width="16" height="16" viewBox="0 0 16 16"><rect x="1.5" y="6" width="8" height="4" rx="2" transform="rotate(-45 5.5 8)" fill="none" stroke="#fff" stroke-width="1.6"/><rect x="6.5" y="6" width="8" height="4" rx="2" transform="rotate(-45 10.5 8)" fill="none" stroke="#fff" stroke-width="1.6"/></svg></span>
    </div>
  </div>
  <div class="gallery-item g4" role="img" aria-label="Photo of a kitchen with wood cabinets and an island"></div>
  <div class="gallery-item g5" role="img" aria-label="Photo of a bathroom with a vanity"></div>
  <div class="gallery-item g6" role="img" aria-label="Photo of built-in wooden mudroom lockers"></div>
  <div class="gallery-item g7" role="img" aria-label="Photo of a fireplace with a mounted television"></div>
  <div class="gallery-item g8" role="img" aria-label="Photo of a kitchen with pendant lights"></div>
</section>

<section>
  <h2 class="abs testimonials-title">Client Testimonials</h2>
  <div class="abs slider-arrow" style="left:90px;top:2459px"><svg width="10" height="14" viewBox="0 0 10 14"><polyline points="8,1 2,7 8,13" fill="none" stroke="#ccc" stroke-width="1.5"/></svg></div>
  <div class="abs slider-arrow" style="left:1079px;top:2459px"><svg width="10" height="14" viewBox="0 0 10 14"><polyline points="2,1 8,7 2,13" fill="none" stroke="#ccc" stroke-width="1.5"/></svg></div>
  <blockquote class="abs quote red">Lorem ipsum dolor sit amet, consectetur adipisicing elit. Enim, delectus atque odit esse harum! Saepe!<span class="quote-tail"></span></blockquote>
  <blockquote class="abs quote grey">Lorem ipsum dolor sit amet, consectetur adipisicing elit. Enim, delectus atque odit esse harum! Saepe!<span class="quote-tail"></span></blockquote>
  <div class="abs author" style="left:201px;top:2514px"><div class="avatar" role="img" aria-label="Client photo"></div><div><div class="author-name">John Doe</div><div class="author-role">Web designer</div></div></div>
  <div class="abs author" style="left:607px;top:2541px"><div class="avatar" role="img" aria-label="Client photo"></div><div><div class="author-name">Jessica Doe</div><div class="author-role">Developer</div></div></div>
</section>

<footer class="abs site-footer"></footer>
<div class="abs footer-map" role="img" aria-label="Faint world map backdrop"></div>
<div class="abs footer-brand"><span class="brand-square"></span><span class="brand-name">Dovin<br>Pratchell<br>Homes</span></div>
<div class="abs footer-rule"></div>
<div class="abs field f-name">Full Name</div>
<div class="abs field f-email">Email</div>
<div class="abs field f-message">Message</div>
<div class="abs btn-send">SEND US A MESSAGE</div>
<h3 class="abs contact-title">CONTACT US</h3>
<div class="abs contact-line c-phone"><svg width="22" height="22" viewBox="0 0 24 24"><circle cx="12" cy="12" r="11" fill="none" stroke="#c1272d" stroke-width="1.5"/><path d="M8.5 10.5a8 8 0 0 0 5 5l1.4-1.4c.2-.2.5-.3.7-.1l1.9.7v2.3c0 .4-.3.7-.7.7A10 10 0 0 1 6.3 7.2c0-.4.3-.7.7-.7h2.3l.7 1.9c.1.3 0 .5-.1.7z" fill="#c1272d"/></svg><span>515.555.0148</span></div>
<div class="abs contact-line c-mail"><svg width="22" height="16" viewBox="0 0 22 16"><rect x="1" y="1" width="20" height="14" fill="#c1272d"/><polyline points="1,1 11,9 21,1" fill="none" stroke="#231f20" stroke-width="1.5"/></svg><span>hello@northfieldworks.com</span></div>
<div class="abs contact-line c-addr"><svg width="18" height="24" viewBox="0 0 18 24"><path d="M9 1a7.5 7.5 0 0 0-7.5 7.5C1.5 14 9 23 9 23s7.5-9 7.5-14.5A7.5 7.5 0 0 0 9 1z" fill="#c1272d"/><circle cx="9" cy="8.5" r="2.8" fill="#231f20"/></svg><span>Northfield Works, Inc.<br>48 Alder Crest Road Ste B<br>Maple Falls WI 54001</span></div>
<p class="abs copyright">Copyright © 2017 Dovin Pratchell. All Right Revered</p>

</body>
</html>
```